Income Tax Business Cards - Updates

Need to update these business cards while keeping all the same wording but just update them and make them look nicer and more modern/ on brand with our brand.

Industry/Entity Type

finance

Contact Information for Business Card

we have multiple locations so will just need to easily be able to change the address and phone numbers

Colors

Designer to choose colors to be used in the design.

```html
<!DOCTYPE html>
<html lang="en">
<head>
<meta charset="utf-8">
<title>Ledgerline Financial Group – Business Cards</title>
<link rel="stylesheet" href="https://fonts.googleapis.com/css2?family=Tinos:wght@400;700&family=Arimo:wght@400;700&display=swap">
<style>
  :root {
    --brand-green: #0e5a30;
    --brand-red: #b51f2a;
    --paper: #f6f6f4;
    --ink: #1f2a24;
    --canvas-bg: #e4e4e1;
    --white: #ffffff;
    --rule: #b9bdb9;
  }
  * { box-sizing: border-box; margin: 0; padding: 0; }
  html, body { width: 1200px; height: 912px; overflow: hidden; }
  body {
    background: var(--canvas-bg);
    position: relative;
    font-family: "Arimo", Arial, sans-serif;
  }
  .card {
    position: absolute;
    width: 580px;
    height: 332px;
    overflow: hidden;
    box-shadow: 0 8px 24px rgba(0,0,0,.18);
  }
  .serif { font-family: "Tinos", "Times New Roman", serif; font-weight: 700; }
  .sans { font-family: "Arimo", Arial, sans-serif; font-weight: 700; }

  /* Front card */
  .card--front { left: 70px; top: 90px; background: var(--brand-green); color: var(--white); }
  .card--front .brand-name {
    position: absolute; left: 0; right: 0; top: 58px;
    text-align: center; font-family: "Tinos", serif; font-weight: 400;
    font-size: 30px; letter-spacing: .5px; color: var(--white);
  }
  .card--front .brand-mark {
    display: inline-block; width: 14px; height: 14px; border-radius: 50%;
    background: var(--white); margin-right: 10px; vertical-align: 3px;
  }
  .card--front .tagline-band {
    position: absolute; left: 0; right: 0; top: 128px; height: 56px;
    background: var(--brand-red);
    display: flex; align-items: center; justify-content: center;
    font-size: 40px;
  }
  .card--front .offer {
    position: absolute; left: 0; right: 0; top: 196px; text-align: center; line-height: 1;
  }
  .card--front .offer-amount { font-size: 64px; }
  .card--front .offer-note { font-size: 40px; margin-top: 8px; }

  /* Back card */
  .card--back { left: 550px; top: 480px; background: var(--paper); color: var(--ink); }
  .card--back .header {
    position: absolute; left: 0; right: 0; top: 0; height: 118px;
    display: flex; align-items: center;
  }
  .card--back .brand-name {
    width: 300px; text-align: center; font-family: "Tinos", serif; font-weight: 400;
    font-size: 26px; color: var(--brand-green);
  }
  .card--back .brand-mark {
    display: inline-block; width: 12px; height: 12px; border-radius: 50%;
    background: var(--brand-green); margin-right: 8px; vertical-align: 2px;
  }
  .card--back .divider { width: 1px; height: 84px; background: var(--rule); }
  .card--back .contact { padding-left: 22px; font-size: 15px; line-height: 1.3; }
  .card--back .contact-phone { display: flex; align-items: center; gap: 8px; font-size: 17px; margin-bottom: 10px; }
  .card--back .tagline-band {
    position: absolute; left: 0; right: 0; top: 128px; height: 54px;
    background: var(--brand-green); color: var(--white);
    display: flex; align-items: center; justify-content: center; font-size: 36px;
  }
  .card--back .offer {
    position: absolute; left: 0; right: 0; top: 196px; text-align: center; line-height: 1;
  }
  .card--back .offer-amount { font-size: 60px; color: var(--brand-green); }
  .card--back .offer-note { font-size: 36px; color: var(--brand-red); margin-top: 6px; }
  .card--back .offer-terms { font-family: "Arimo", sans-serif; font-weight: 400; font-size: 20px; margin-top: 6px; }
</style>
</head>
<body>

  <section class="card card--front" aria-label="Business card front">
    <div class="brand-name"><span class="brand-mark"></span>Ledgerline Financial Group</div>
    <div class="tagline-band serif">File your Taxes here</div>
    <div class="offer">
      <div class="offer-amount sans">UP to $6000</div>
      <div class="offer-note serif">Same day advance</div>
    </div>
  </section>

  <section class="card card--back" aria-label="Business card back">
    <div class="header">
      <div class="brand-name"><span class="brand-mark"></span>Ledgerline Financial Group</div>
      <div class="divider"></div>
      <div class="contact">
        <div class="contact-phone">
          <svg width="14" height="14" viewBox="0 0 24 24" aria-hidden="true">
            <path fill="#1f2a24" d="M6.6 10.8a15.1 15.1 0 0 0 6.6 6.6l2.2-2.2a1 1 0 0 1 1-.25 11.4 11.4 0 0 0 3.6.57 1 1 0 0 1 1 1V20a1 1 0 0 1-1 1A17 17 0 0 1 3 4a1 1 0 0 1 1-1h3.5a1 1 0 0 1 1 1c0 1.25.2 2.45.57 3.57a1 1 0 0 1-.25 1z"/>
          </svg>
          <span>(555) 014-2290</span>
        </div>
        <div class="contact-address">4127 Harborview Lane<br>Maple Grove, NY 11020</div>
      </div>
    </div>
    <div class="tagline-band serif">Free Estimates!</div>
    <div class="offer">
      <div class="offer-amount sans">UP to $6000</div>
      <div class="offer-note serif">Same day advance</div>
      <div class="offer-terms">on approved tax returns!</div>
    </div>
  </section>

</body>
</html>
```